Ironbark lane plumbing plumbing company business card design

Something sinilar to business card i upload it is my old business card design
And have a good watermark with the logo or majority of the logot in rhe background as watermark

Plumbing business similar to uploaded design with a nice watermark of the logo

Font styles to use
Script

Colors

Designer to choose colors to be used in the design.

```html
<!DOCTYPE html>
<html lang="en">
<head>
<meta charset="utf-8">
<title>Ironbark Lane Plumbing – Business Card</title>
<link href="https://fonts.googleapis.com/css2?family=Montserrat:wght@500;700;800;900&family=Dancing+Script:wght@600;700&display=swap" rel="stylesheet">
<style>
  :root {
    --ink: #07060a;
    --blue: #0a74bf;
    --paper: #ffffff;
    --stage: #e6e7e9;
    --mark-dark: rgba(70, 95, 130, 0.45);
    --mark-grey: rgba(120, 120, 128, 0.8);
  }
  * { box-sizing: border-box; margin: 0; padding: 0; }
  html, body { width: 1200px; height: 1200px; overflow: hidden; }
  body {
    background: var(--stage);
    font-family: "Montserrat", Arial, sans-serif;
    display: flex;
    flex-direction: column;
    align-items: center;
    justify-content: center;
    gap: 40px;
  }
  .card {
    position: relative;
    width: 900px;
    height: 540px;
    background: var(--paper);
    overflow: hidden;
    box-shadow: 0 6px 18px rgba(0,0,0,0.18);
  }
  .card__art { position: absolute; inset: 0; width: 100%; height: 100%; }

  /* front */
  .brand {
    position: absolute;
    top: 188px;
    left: 430px;
    width: 440px;
    text-align: center;
  }
  .brand__name {
    font-weight: 800;
    font-size: 40px;
    line-height: 1.1;
    letter-spacing: 3px;
    text-transform: uppercase;
    color: var(--ink);
  }
  .web-line {
    position: absolute;
    right: 60px;
    bottom: 50px;
    font-family: "Dancing Script", cursive;
    font-weight: 700;
    font-size: 25px;
    color: var(--ink);
  }
  .web-line__domain { color: var(--blue); text-transform: uppercase; }

  /* back */
  .person { position: absolute; top: 70px; left: 79px; }
  .person__name {
    font-size: 46px;
    line-height: 1;
    color: var(--blue);
    font-weight: 500;
  }
  .person__name strong { font-weight: 800; }
  .person__role {
    margin-top: 6px;
    font-size: 23px;
    font-weight: 700;
    color: var(--ink);
  }
  .person__rule {
    margin-top: 20px;
    width: 258px;
    height: 3px;
    background: var(--blue);
  }
  .contacts {
    position: absolute;
    left: 79px;
    top: 225px;
    list-style: none;
    display: flex;
    flex-direction: column;
    gap: 26px;
  }
  .contact { display: flex; align-items: center; gap: 14px; }
  .contact__icon { width: 56px; height: 56px; flex: none; }
  .contact__text {
    border-left: 2px solid var(--blue);
    padding-left: 10px;
    font-family: "Dancing Script", cursive;
    font-weight: 700;
    font-size: 20px;
    line-height: 1.2;
    color: var(--blue);
  }
</style>
</head>
<body>

  <!-- Front of card -->
  <section class="card card--front">
    <svg class="card__art" viewBox="0 0 740 445" preserveAspectRatio="none" aria-hidden="true">
      <rect width="740" height="445" fill="var(--blue)"/>
      <path d="M255 0 C175 90 170 215 220 290 C260 350 300 400 280 445 H0 V0 Z" fill="var(--ink)"/>
      <path d="M305 0 H740 V445 H330 C355 400 315 345 272 290 C218 215 225 90 305 0 Z" fill="var(--paper)"/>
      <text x="25" y="430" font-family="Montserrat, sans-serif" font-weight="900" font-size="175" fill="var(--mark-dark)">ILP</text>
    </svg>
    <div class="brand">
      <p class="brand__name">Ironbark Lane Plumbing</p>
    </div>
    <p class="web-line">www.<span class="web-line__domain">ironbarklaneplumbing</span>.com</p>
  </section>

  <!-- Back of card -->
  <section class="card card--back">
    <svg class="card__art" viewBox="0 0 740 445" preserveAspectRatio="none" aria-hidden="true">
      <rect width="740" height="445" fill="var(--paper)"/>
      <path d="M385 0 C490 90 515 200 455 300 C415 365 375 410 380 445 H740 V0 Z" fill="var(--blue)"/>
      <path d="M440 0 C540 80 560 200 500 300 C460 370 420 410 430 445 H740 V0 Z" fill="var(--ink)"/>
      <text x="370" y="440" font-family="Montserrat, sans-serif" font-weight="900" font-size="175" fill="var(--mark-grey)" opacity="0.55">ILP</text>
    </svg>

    <div class="person">
      <h1 class="person__name"><strong>NAME</strong> HERE</h1>
      <p class="person__role">DESIGNATION</p>
      <div class="person__rule"></div>
    </div>

    <ul class="contacts">
      <li class="contact">
        <svg class="contact__icon" viewBox="0 0 56 56" aria-hidden="true">
          <rect x="2" y="2" width="52" height="52" rx="12" fill="var(--ink)"/>
          <path d="M2 32 H54 V42 A12 12 0 0 1 42 54 H14 A12 12 0 0 1 2 42 Z" fill="var(--blue)"/>
          <circle cx="28" cy="28" r="16" fill="none" stroke="#fff" stroke-width="3"/>
          <path d="M21 20 l4 -2 l3 6 l-3 2 c1 3 3 5 6 6 l2 -3 l6 3 l-2 4 c-9 0 -16 -7 -16 -16 z" fill="#fff"/>
        </svg>
        <p class="contact__text">000 000 0000<br>000 000 0000</p>
      </li>
      <li class="contact">
        <svg class="contact__icon" viewBox="0 0 56 56" aria-hidden="true">
          <rect x="2" y="2" width="52" height="52" rx="12" fill="var(--ink)"/>
          <path d="M2 32 H54 V42 A12 12 0 0 1 42 54 H14 A12 12 0 0 1 2 42 Z" fill="var(--blue)"/>
          <rect x="12" y="16" width="32" height="24" rx="2" fill="#fff"/>
          <path d="M12 17 L28 30 L44 17" fill="none" stroke="var(--ink)" stroke-width="3"/>
        </svg>
        <p class="contact__text">hello@ironbarklaneplumbing.com</p>
      </li>
      <li class="contact">
        <svg class="contact__icon" viewBox="0 0 56 56" aria-hidden="true">
          <rect x="2" y="2" width="52" height="52" rx="12" fill="var(--ink)"/>
          <path d="M2 32 H54 V42 A12 12 0 0 1 42 54 H14 A12 12 0 0 1 2 42 Z" fill="var(--blue)"/>
          <g fill="none" stroke="#fff" stroke-width="2.5">
            <circle cx="28" cy="28" r="15"/>
            <ellipse cx="28" cy="28" rx="7" ry="15"/>
            <line x1="13" y1="28" x2="43" y2="28"/>
            <line x1="15" y1="21" x2="41" y2="21"/>
            <line x1="15" y1="35" x2="41" y2="35"/>
          </g>
        </svg>
        <p class="contact__text">www.ironbarklaneplumbing.com</p>
      </li>
    </ul>
  </section>

</body>
</html>
```